Chic, award winning Billboard wanted

Our restaurant is a modern and chic restaurant with AWESOME service, Fresh seafood and aged steaks in Costa Rica (where great service is a rarity as well as refined cooking).
The restaurant is called K Seafood & Grill, located in Manuel Antonio, Costa Rica
Our current marketing line is "K is not just dinner, it's a whole evening" Our colours are Pantone u498 blue and black as background
Go to our web site to see our style www.Kseafoodgrillrica.com
We have secured a 3.5 metre high by 9 metre wide billboard on the main highway and looking for an outstanding design to drive traffic to our business.
People associate Seafood too much with our restaurant, so we want to have our logo very present, but have the words "seafood"; "grill"; "aged steaks"; "lounge" kind of floating around the Z so that people don't associate our restaurant with only one type of food.
REMEMBER THIS BILLBOARD IS ON A MAIN HIGHWAY THAT PEOPLE ARE TRAVELLING AT 55 MILES PER HOUR!
check out our voyageranks for customer reviews: http://www.voyageranks.com/Eatery_Review-g551832-d7730194-Reviews-K_Seafood_Grill-Manuel_Antonio_National_Park_Province_of_Puntarenas.html
Target Market(s)
Travelling American & European Tourists to National Park,
Other font styles liked:
- Century Gothic
Requirements
Must have
- Want a fun and interesting billboard that engages people, not a static information "Logo, name, phone number"
- Needs to have phone number: 2615-3082
- Needs to have Voyageranks logo
Nice to have
- See attached ad done for a local magazine for the "look"

```html
<!DOCTYPE html>
<html lang="en">
<head>
<meta charset="utf-8">
<title>K Seafood &amp; Grill — Billboard</title>
<link rel="stylesheet" href="https://fonts.googleapis.com/css2?family=Questrial&family=Nunito:wght@700;800;900&family=Asap+Condensed:wght@500;700&display=swap">
<style>
  :root {
    --page: #ffffff;
    --ink: #0d0d0d;
    --brand-blue: #49c6ef;
    --frame-grey: #9ea3a8;
    --text-light: #ffffff;
    --band: rgba(150, 150, 150, 0.5);
    --outline: #0e1f2b;
    --halo: #ffffff;
  }
  html, body {
    margin: 0;
    padding: 0;
    width: 1200px;
    height: 1000px;
    overflow: hidden;
    background: var(--page);
  }
  .canvas {
    position: relative;
    width: 1200px;
    height: 1000px;
  }
  .billboard {
    position: absolute;
    left: 57px;
    top: 283px;
    width: 1086px;
    height: 434px;
    background: var(--ink);
  }

  /* Brand panel */
  .brand-panel {
    position: absolute;
    left: 0;
    top: 0;
    width: 330px;
    height: 434px;
    background: var(--ink);
  }
  .brand-frame {
    position: absolute;
    left: 29px;
    top: 16px;
    width: 273px;
    height: 288px;
    border: 2px solid var(--frame-grey);
    box-sizing: border-box;
  }
  .brand-name {
    margin: 0;
    font-family: "Questrial", "Century Gothic", sans-serif;
    font-weight: 400;
    color: var(--brand-blue);
    text-transform: uppercase;
  }
  .brand-initial {
    position: absolute;
    left: 0;
    right: 0;
    top: 14px;
    text-align: center;
    font-size: 230px;
    line-height: 220px;
  }
  .brand-words {
    position: absolute;
    left: 0;
    right: 0;
    top: 248px;
    text-align: center;
    font-size: 26px;
    line-height: 1;
    letter-spacing: 1px;
  }
  .tagline {
    position: absolute;
    left: 18px;
    top: 350px;
    margin: 0;
    font-family: "Asap Condensed", "Century Gothic", sans-serif;
    font-weight: 500;
    color: var(--text-light);
    font-size: 19px;
    line-height: 32px;
    text-transform: uppercase;
    white-space: nowrap;
  }
  .tagline .accent {
    color: var(--brand-blue);
    font-size: 29px;
    font-weight: 700;
  }

  /* Photo panel */
  .scene {
    position: absolute;
    left: 331px;
    top: 0;
    width: 755px;
    height: 434px;
    background:
      radial-gradient(ellipse 22% 32% at 48% 48%, rgba(196, 140, 100, 0.75), rgba(0,0,0,0) 100%),
      radial-gradient(ellipse 18% 30% at 78% 48%, rgba(190, 130, 95, 0.7), rgba(0,0,0,0) 100%),
      radial-gradient(ellipse 16% 28% at 22% 50%, rgba(200, 160, 110, 0.65), rgba(0,0,0,0) 100%),
      radial-gradient(ellipse 20% 40% at 8% 85%, rgba(170, 100, 60, 0.8), rgba(0,0,0,0) 100%),
      radial-gradient(ellipse 45% 18% at 55% 90%, rgba(220, 210, 195, 0.35), rgba(0,0,0,0) 100%),
      radial-gradient(ellipse 14% 24% at 30% 22%, rgba(90, 150, 80, 0.7), rgba(0,0,0,0) 100%),
      radial-gradient(ellipse 12% 22% at 62% 22%, rgba(80, 140, 110, 0.6), rgba(0,0,0,0) 100%),
      linear-gradient(180deg, #14201a 0%, #201a14 50%, #2e2017 100%);
  }
  .menu-band {
    position: absolute;
    left: 0;
    top: 6px;
    width: 755px;
    height: 56px;
    background: var(--band);
    display: flex;
    align-items: center;
    justify-content: center;
    gap: 5px;
  }
  .outlined {
    font-family: "Nunito", "Arial Rounded MT Bold", sans-serif;
    font-weight: 900;
    color: var(--brand-blue);
    text-shadow:
      -2px -2px 0 var(--outline), 2px -2px 0 var(--outline),
      -2px 2px 0 var(--outline), 2px 2px 0 var(--outline),
      0 -2px 0 var(--outline), 0 2px 0 var(--outline),
      -2px 0 0 var(--outline), 2px 0 0 var(--outline),
      -3px -3px 0 var(--halo), 3px -3px 0 var(--halo),
      -3px 3px 0 var(--halo), 3px 3px 0 var(--halo),
      0 -3px 0 var(--halo), 0 3px 0 var(--halo),
      -3px 0 0 var(--halo), 3px 0 0 var(--halo);
  }
  .menu-item { font-size: 37px; line-height: 1; letter-spacing: 0.5px; }
  .menu-divider {
    width: 2px;
    height: 42px;
    background: var(--outline);
    box-shadow: 0 0 0 1px var(--halo);
  }
  .invite {
    position: absolute;
    left: 150px;
    width: 500px;
    top: 262px;
    text-align: center;
  }
  .invite-title {
    margin: 0;
    font-size: 33px;
    line-height: 1;
  }
  .invite-body {
    margin: 4px 0 0;
    font-family: "Nunito", "Arial Rounded MT Bold", sans-serif;
    font-weight: 900;
    font-size: 16px;
    line-height: 21px;
    color: var(--brand-blue);
    text-shadow:
      -1.5px -1.5px 0 var(--outline), 1.5px -1.5px 0 var(--outline),
      -1.5px 1.5px 0 var(--outline), 1.5px 1.5px 0 var(--outline),
      0 -1.5px 0 var(--outline), 0 1.5px 0 var(--outline),
      -1.5px 0 0 var(--outline), 1.5px 0 0 var(--outline),
      0 0 3px var(--halo);
  }
  .review-listing {
    position: absolute;
    left: 670px;
    top: 344px;
    display: flex;
    flex-direction: column;
    align-items: center;
    gap: 3px;
  }
  .review-mark {
    width: 26px;
    height: 26px;
    border-radius: 50%;
    border: 3px solid var(--text-light);
  }
  .review-name {
    font-family: "Nunito", sans-serif;
    font-weight: 700;
    font-size: 15px;
    color: var(--text-light);
  }
  .reservations {
    position: absolute;
    right: 13px;
    top: 402px;
    margin: 0;
    font-family: "Nunito", sans-serif;
    font-weight: 800;
    font-size: 16px;
    color: var(--text-light);
    text-shadow: 0 1px 2px #000, 0 0 4px #000;
  }
</style>
</head>
<body>
<div class="canvas">
  <section class="billboard">
    <div class="brand-panel">
      <div class="brand-frame">
        <h1 class="brand-name">
          <span class="brand-initial">K</span>
          <span class="brand-words">Seafood &amp; Grill</span>
        </h1>
      </div>
      <p class="tagline">
        <span class="accent">K</span> is <span class="accent">not</span> just dinner,<br>
        it's a <span class="accent">whole</span> evening
      </p>
    </div>

    <div class="scene" role="img" aria-label="Photo of friends laughing around a dinner table with drinks and plates in a softly lit restaurant">
      <div class="menu-band">
        <span class="menu-item outlined">Seafood</span>
        <span class="menu-divider"></span>
        <span class="menu-item outlined">Grill</span>
        <span class="menu-divider"></span>
        <span class="menu-item outlined">Aged Steaks</span>
        <span class="menu-divider"></span>
        <span class="menu-item outlined">Lounge</span>
      </div>

      <div class="invite">
        <p class="invite-title outlined">Come and join us</p>
        <p class="invite-body">Tonight In Our Hardwood Floor Dining Or Our Beach<br>Sand Bar For A Drink And An Unforgetable<br>Experience.</p>
      </div>

      <div class="review-listing">
        <span class="review-mark"></span>
        <span class="review-name">voyageranks</span>
      </div>

      <p class="reservations">Call for reservations : 2615-3082</p>
    </div>
  </section>
</div>
</body>
</html>
```